Korvanta Corporate Vision Mission Statement Infographic

We need an info graphic which summarizes and visually explains the companies Ambition Statement, Strategic Priorities, Principles and Brand Actions and how they relate to each other

Need extra days to review

```html
<!DOCTYPE html>
<html lang="en">
<head>
<meta charset="utf-8">
<title>Korvanta – Vision &amp; Principles</title>
<link href="https://fonts.googleapis.com/css2?family=League+Spartan:wght@500;600;700&family=Lato:wght@400;700&display=swap" rel="stylesheet">
<style>
  :root{
    --bg:#e4eaf5;
    --white:#ffffff;
    --blue:#4a6fb5;
    --blue-light:#7aa2dd;
    --orange:#ff6a1a;
  }
  html,body{margin:0;padding:0;overflow:hidden;background:var(--white);}
  .canvas{width:765px;height:1200px;position:relative;overflow:hidden;}
  .canvas svg{display:block;}
  .head{font-family:"League Spartan",sans-serif;font-weight:600;}
  .body{font-family:"Lato",sans-serif;}
  .tagline{fill:var(--blue);font-size:39px;}
  .brand-name{fill:var(--blue);font-size:28px;font-weight:700;}
  .brand-sub{fill:var(--blue);font-size:9.5px;letter-spacing:1.4px;}
  .section-title{fill:var(--white);font-size:38px;}
  .ambition-text{fill:var(--white);font-size:16px;}
  .priority-box-text{fill:var(--white);font-size:30px;font-weight:700;}
  .pill-text{fill:var(--white);font-size:17.5px;}
  .principles-title{fill:var(--blue);font-size:46px;font-weight:700;}
  .node-label{fill:var(--white);font-size:16px;}
  .centre-label{fill:var(--white);font-size:21px;}
  .tag-text{fill:var(--white);font-size:9.5px;}
  .ba-text{fill:var(--white);font-size:7px;}
</style>
</head>
<body>
<div class="canvas">
<svg width="765" height="1200" viewBox="0 0 765 1200" xmlns="http://www.w3.org/2000/svg">
  <!-- section backgrounds -->
  <rect x="0" y="0" width="765" height="326" fill="var(--bg)"/>
  <rect x="0" y="358" width="765" height="360" fill="var(--bg)"/>
  <rect x="0" y="758" width="765" height="410" fill="var(--bg)"/>

  <!-- brand -->
  <text class="head brand-name" x="36" y="56">Korvanta</text>
  <text class="body brand-sub" x="38" y="71">INSURANCE SERVICES</text>
  <text class="head tagline" x="256" y="68">Dream. Explore. Travel On.</text>

  <!-- ambition -->
  <rect x="0" y="152" width="90" height="82" fill="var(--blue-light)"/>
  <polygon points="352,153 370,153 392,190 374,190" fill="var(--blue-light)"/>
  <polygon points="364,153 382,153 404,190 386,190" fill="var(--blue-light)"/>
  <polygon points="83,134 307,134 340,190 83,190" fill="var(--orange)"/>
  <text class="head section-title" x="94" y="180">AMBITION</text>
  <polygon points="82,190 550,190 617,286 82,286" fill="var(--blue)"/>
  <polygon points="566,190 590,190 659,286 635,286" fill="var(--blue)"/>
  <text class="body ambition-text" x="93" y="218">Our dream is to be a globally recognized travel protection</text>
  <text class="body ambition-text" x="93" y="240">provider with heart — strive to be the best in the eyes of our</text>
  <text class="body ambition-text" x="93" y="262">customers as they travel and explore the world safely.</text>

  <!-- strategic priorities -->
  <rect x="112" y="428" width="68" height="68" rx="6" fill="var(--blue)" opacity="0.35" role="img" aria-label="Presenter with audience icon"/>
  <rect x="46" y="502" width="194" height="82" fill="var(--blue)"/>
  <rect x="51" y="507" width="184" height="72" fill="none" stroke="var(--white)" stroke-width="2"/>
  <text class="head priority-box-text" x="143" y="540" text-anchor="middle">STRATEGIC</text>
  <text class="head priority-box-text" x="143" y="570" text-anchor="middle">PRIORITIES</text>

  <g stroke="var(--blue-light)" stroke-width="2.5" fill="none">
    <line x1="267" y1="449" x2="267" y2="645"/>
    <line x1="240" y1="550" x2="330" y2="550"/>
    <line x1="267" y1="449" x2="330" y2="449"/>
    <line x1="267" y1="645" x2="330" y2="645"/>
  </g>
  <g fill="var(--white)" stroke="var(--blue)" stroke-width="2.5">
    <circle cx="267" cy="449" r="7"/><circle cx="267" cy="550" r="7"/><circle cx="267" cy="645" r="7"/>
  </g>
  <g fill="var(--blue)"><circle cx="267" cy="449" r="3"/><circle cx="267" cy="550" r="3"/><circle cx="267" cy="645" r="3"/></g>

  <!-- pill 1 -->
  <rect x="322" y="421" width="425" height="61" rx="30.5" fill="none" stroke="var(--blue)" stroke-width="3"/>
  <rect x="330" y="428" width="408" height="47" rx="23.5" fill="var(--blue)"/>
  <circle cx="353" cy="451" r="38" fill="var(--white)"/>
  <circle cx="353" cy="451" r="31" fill="var(--blue)" role="img" aria-label="Hand holding person icon"/>
  <text class="head pill-text" x="401" y="457">TRANSFORM THE CUSTOMER EXPERIENCE</text>
  <!-- pill 2 -->
  <rect x="322" y="518" width="425" height="61" rx="30.5" fill="none" stroke="var(--orange)" stroke-width="3"/>
  <rect x="330" y="525" width="408" height="47" rx="23.5" fill="var(--orange)"/>
  <circle cx="353" cy="548" r="38" fill="var(--white)"/>
  <circle cx="353" cy="548" r="31" fill="var(--orange)" role="img" aria-label="Tangled line becoming arrow icon"/>
  <text class="head pill-text" x="401" y="554">SIMPLIFY THE COMPLEX</text>
  <!-- pill 3 -->
  <rect x="322" y="614" width="425" height="61" rx="30.5" fill="none" stroke="var(--blue)" stroke-width="3"/>
  <rect x="330" y="621" width="408" height="47" rx="23.5" fill="var(--blue)"/>
  <circle cx="353" cy="644" r="38" fill="var(--white)"/>
  <circle cx="353" cy="644" r="31" fill="var(--blue)" role="img" aria-label="Group of partners icon"/>
  <text class="head pill-text" x="401" y="650">BUILD SUCCESSFUL PARTNERSHIPS</text>

  <!-- principles -->
  <text class="head principles-title" x="392" y="812" text-anchor="middle">PRINICPLES &amp; BRAND ACTIONS</text>

  <!-- spokes -->
  <g stroke="var(--blue)" stroke-width="3">
    <line x1="378" y1="934" x2="378" y2="980"/>
    <line x1="258" y1="978" x2="315" y2="1025"/>
    <line x1="506" y1="978" x2="450" y2="1025"/>
    <line x1="258" y1="1098" x2="315" y2="1050"/>
    <line x1="506" y1="1098" x2="450" y2="1050"/>
    <line x1="378" y1="872" x2="378" y2="910"/>
  </g>

  <!-- centre -->
  <circle cx="378" cy="1038" r="68" fill="none" stroke="var(--blue)" stroke-width="3"/>
  <circle cx="378" cy="1038" r="60" fill="none" stroke="var(--orange)" stroke-width="6"/>
  <circle cx="378" cy="1038" r="50" fill="var(--white)" stroke="var(--blue)" stroke-width="6"/>
  <circle cx="378" cy="1106" r="4" fill="var(--blue)"/>
  <rect x="300" y="1022" width="154" height="33" rx="3" fill="var(--blue)" stroke="var(--white)" stroke-width="2"/>
  <text class="head centre-label" x="377" y="1046" text-anchor="middle">PRINCIPLES</text>

  <!-- independence -->
  <rect x="329" y="833" width="98" height="17" rx="2" fill="var(--blue-light)"/>
  <text class="body tag-text" x="378" y="845" text-anchor="middle">Be extraordinary</text>
  <rect x="338" y="853" width="22" height="32" rx="3" fill="var(--blue)" opacity="0.35" role="img" aria-label="Cheering figure icon"/>
  <rect x="396" y="853" width="22" height="32" rx="3" fill="var(--blue)" opacity="0.35" role="img" aria-label="Cheering figure icon"/>
  <circle cx="378" cy="872" r="7" fill="var(--white)" stroke="var(--orange)" stroke-width="2.5"/>
  <rect x="316" y="886" width="126" height="24" fill="var(--orange)"/>
  <text class="head node-label" x="379" y="904" text-anchor="middle">INDEPENDENCE</text>

  <!-- node discs -->
  <g fill="var(--white)" stroke="var(--blue)" stroke-width="3">
    <circle cx="378" cy="934" r="18"/>
    <circle cx="258" cy="978" r="18"/>
    <circle cx="506" cy="978" r="18"/>
    <circle cx="258" cy="1098" r="18"/>
    <circle cx="506" cy="1098" r="18"/>
  </g>
  <g fill="var(--blue)">
    <circle cx="378" cy="934" r="5"/>
    <circle cx="258" cy="978" r="5"/>
    <circle cx="506" cy="978" r="5"/>
    <circle cx="258" cy="1098" r="5"/>
    <circle cx="506" cy="1098" r="5"/>
  </g>

  <!-- integrity -->
  <rect x="178" y="906" width="48" height="50" rx="6" fill="var(--blue)" opacity="0.35" role="img" aria-label="Head with scales of justice icon"/>
  <rect x="144" y="967" width="96" height="23" fill="var(--orange)"/>
  <text class="head node-label" x="195" y="984" text-anchor="middle">INTEGRITY</text>
  <line x1="128" y1="1009" x2="158" y2="1009" stroke="var(--blue)" stroke-width="2"/>
  <rect x="32" y="1001" width="96" height="16" rx="2" fill="var(--blue-light)"/>
  <text class="body tag-text" x="80" y="1012" text-anchor="middle">Do the right thing</text>
  <rect x="155" y="1002" width="79" height="14" fill="var(--blue)"/>
  <text class="body ba-text" x="199" y="1012" text-anchor="middle">BRAND ACTION</text>
  <circle cx="157" cy="1009" r="7" fill="var(--white)" stroke="var(--orange)" stroke-width="2"/>

  <!-- excellence -->
  <rect x="555" y="910" width="42" height="52" rx="6" fill="var(--blue)" opacity="0.35" role="img" aria-label="Award rosette icon"/>
  <rect x="520" y="967" width="110" height="23" fill="var(--orange)"/>
  <text class="head node-label" x="576" y="984" text-anchor="middle">EXCELLENCE</text>
  <rect x="544" y="1002" width="77" height="14" fill="var(--blue)"/>
  <text class="body ba-text" x="580" y="1012" text-anchor="middle">BRAND ACTION</text>
  <line x1="627" y1="1009" x2="646" y2="1009" stroke="var(--blue)" stroke-width="2"/>
  <circle cx="620" cy="1009" r="7" fill="var(--white)" stroke="var(--orange)" stroke-width="2"/>
  <rect x="646" y="1001" width="98" height="16" rx="2" fill="var(--blue-light)"/>
  <text class="body tag-text" x="695" y="1012" text-anchor="middle">Embrace challenge</text>

  <!-- commitment -->
  <rect x="154" y="1048" width="64" height="32" rx="6" fill="var(--blue)" opacity="0.35" role="img" aria-label="Handshake icon"/>
  <rect x="126" y="1087" width="114" height="23" fill="var(--orange)"/>
  <text class="head node-label" x="185" y="1104" text-anchor="middle">COMMITMENT</text>
  <line x1="106" y1="1128" x2="140" y2="1128" stroke="var(--blue)" stroke-width="2"/>
  <rect x="10" y="1120" width="96" height="16" rx="2" fill="var(--blue-light)"/>
  <text class="body tag-text" x="58" y="1131" text-anchor="middle">Go the extra mile</text>
  <rect x="138" y="1121" width="79" height="14" fill="var(--blue)"/>
  <text class="body ba-text" x="182" y="1131" text-anchor="middle">BRAND ACTION</text>
  <circle cx="139" cy="1128" r="7" fill="var(--white)" stroke="var(--orange)" stroke-width="2"/>

  <!-- compassion -->
  <rect x="559" y="1040" width="42" height="42" rx="6" fill="var(--blue)" opacity="0.35" role="img" aria-label="Hands holding heart icon"/>
  <rect x="520" y="1087" width="118" height="23" fill="var(--orange)"/>
  <text class="head node-label" x="580" y="1104" text-anchor="middle">COMPASSION</text>
  <rect x="552" y="1121" width="72" height="14" fill="var(--blue)"/>
  <text class="body ba-text" x="586" y="1131" text-anchor="middle">BRAND ACTION</text>
  <line x1="631" y1="1128" x2="656" y2="1128" stroke="var(--blue)" stroke-width="2"/>
  <circle cx="627" cy="1128" r="7" fill="var(--white)" stroke="var(--orange)" stroke-width="2"/>
  <rect x="656" y="1120" width="98" height="16" rx="2" fill="var(--blue-light)"/>
  <text class="body tag-text" x="705" y="1131" text-anchor="middle">Put people first</text>
</svg>
</div>
</body>
</html>
```